Corvenix Business Card

Our mission is to craft high value solutions combining consulting and edge technologies for helping big and middle sized companies in the Digital Transformation Process that they must face. We think that this transformation will impact business processes and people skills in a new manner. Corvenix's value proposition is to collaborate with our clients for creating new competitive advantages based on technology, processes and people.
We already have a logo designed through your platform.

Industry/Entity Type

Business

```html
<!DOCTYPE html>
<html lang="en">
<head>
<meta charset="UTF-8">
<title>Corvenix Business Card</title>
<link rel="stylesheet" href="https://fonts.googleapis.com/css2?family=Roboto:wght@400;500;700&family=Roboto+Condensed:wght@700&display=swap">
<style>
  :root {
    --canvas: #e6e7e9;
    --card: #333334;
    --accent: #29b6ea;
    --accent-deep: #1592c9;
    --white: #ffffff;
    --muted: #e8e8e8;
  }
  * { box-sizing: border-box; margin: 0; padding: 0; }
  html, body {
    width: 1200px;
    height: 1000px;
    overflow: hidden;
    background: var(--canvas);
    font-family: "Roboto", Arial, sans-serif;
  }
  .card {
    position: absolute;
    left: 250px;
    width: 700px;
    height: 400px;
    background: var(--card);
    overflow: hidden;
    box-shadow: 0 8px 24px rgba(0,0,0,0.25);
  }
  .card--front { top: 60px; }
  .card--back { top: 530px; }
  .card__band {
    position: absolute;
    left: 0; right: 0; bottom: 0;
    height: 16px;
    background: linear-gradient(to bottom, var(--accent), var(--accent-deep));
  }
  .brand {
    position: absolute;
    display: flex;
    align-items: center;
    color: var(--white);
    font-weight: 500;
    letter-spacing: 0.04em;
  }
  .brand__dot {
    border-radius: 50%;
    background: var(--accent);
    flex: none;
  }
  .card--front .brand { left: 90px; top: 140px; font-size: 68px; gap: 28px; }
  .card--front .brand__dot { width: 96px; height: 96px; }
  .card--back .brand { left: 40px; top: 110px; font-size: 36px; gap: 16px; }
  .card--back .brand__dot { width: 52px; height: 52px; }

  .contact {
    position: absolute;
    left: 400px;
    top: 48px;
    color: var(--white);
  }
  .contact__name {
    font-family: "Roboto Condensed", "Arial Narrow", sans-serif;
    font-weight: 700;
    font-size: 30px;
    color: var(--accent);
    letter-spacing: 0.02em;
  }
  .contact__title { font-size: 19px; margin-top: 2px; }
  .contact__list { list-style: none; margin-top: 38px; }
  .contact__item {
    display: flex;
    align-items: center;
    gap: 14px;
    font-size: 20px;
    margin-bottom: 12px;
  }
  .contact__icon { width: 30px; height: 30px; flex: none; }
  .contact__company {
    font-weight: 700;
    font-size: 22px;
    margin-top: 30px;
  }
  .contact__address {
    font-style: normal;
    color: var(--accent);
    font-size: 21px;
    line-height: 1.3;
    margin-top: 4px;
  }
</style>
</head>
<body>
  <section class="card card--front" aria-label="Card front">
    <div class="brand"><span class="brand__dot"></span>CORVENIX</div>
    <div class="card__band"></div>
  </section>

  <section class="card card--back" aria-label="Card back">
    <div class="brand"><span class="brand__dot"></span>CORVENIX</div>
    <div class="contact">
      <h1 class="contact__name">YOUR NAME</h1>
      <p class="contact__title">Title</p>
      <ul class="contact__list">
        <li class="contact__item">
          <svg class="contact__icon" viewBox="0 0 30 30" aria-hidden="true">
            <circle cx="15" cy="15" r="15" fill="var(--accent)"/>
            <path d="M10.5 8.5l2.6-.6 1.5 3.6-1.7 1.3c.9 1.8 2.3 3.2 4.1 4.1l1.3-1.7 3.6 1.5-.6 2.6c-.2.7-.8 1.1-1.5 1.1-5.5-.3-9.9-4.7-10.2-10.2 0-.7.4-1.3 .9-1.7z" fill="var(--card)"/>
          </svg>
          123 456 7890
        </li>
        <li class="contact__item">
          <svg class="contact__icon" viewBox="0 0 30 30" aria-hidden="true">
            <circle cx="15" cy="15" r="15" fill="var(--accent)"/>
            <rect x="8" y="10" width="14" height="10" rx="1" fill="var(--card)"/>
            <path d="M8.5 10.5l6.5 5 6.5-5" fill="none" stroke="var(--accent)" stroke-width="1.4"/>
          </svg>
          yourname@corvenix.com
        </li>
      </ul>
      <p class="contact__company">CORVENIX.</p>
      <address class="contact__address">P.O. Box 123 Suite 1, NY<br>TX 1234</address>
    </div>
    <div class="card__band"></div>
  </section>
</body>
</html>
```